Copper Dunes Website design

Create a sophisticated minimalist shopify ecommerce store that can be integrated with retail express POS.

Copper Dunes is a Brick and mortar store that is focused on exceptional customer service and quality Ladies fashion and specialty swimwear for Women, Men and Children.

This website will need to be easy to navigate by the end user and manage inhouse.

With so many different product categories and customer demographics it will be difficult to make seamless and easy to navigate.

Think The Lumora, Pelko etc where there are Women, Men and Kids

It would be fantastic to build a site with three different navigations to constant themes that are modified to suit each demographic.

We have a logo to use and would like the theme to be easily updated as seasons change and our business evolves.

The website must be set up to use SEO for brixel and other leading search engines.

Stock will be supplied from either our brick and mortar store or warehouse so would need to consist of multiple store locations as far as the back end is concerned.

It will need to be set up with apps that allow us to stream line our fullfilment in house (label printing, picking lists and shipping with Rivo Mail)

```html
<!DOCTYPE html>
<html lang="en">
<head>
<meta charset="utf-8">
<title>Copper Dunes — Fashion & Swimwear</title>
<link href="https://fonts.googleapis.com/css2?family=Lato:wght@400;700;900&family=Mulish:wght@300;400;700;800&family=Barlow+Semi+Condensed:wght@500;600;700&display=swap" rel="stylesheet">
<style>
:root{
  --ink:#1d1d1d;
  --olive:#6f7b5c;
  --olive-dark:#5f6b4e;
  --band:#e4e4e2;
  --text:#2b2b2b;
  --muted:#5a5a5a;
  --line:#e2e2e2;
  --white:#ffffff;
  --footer:#ececec;
}
*{box-sizing:border-box;margin:0;padding:0}
html,body{width:1200px;height:5259px;overflow:hidden}
body{font-family:"Lato",sans-serif;color:var(--text);background:var(--white);position:relative}
.abs{position:absolute}
.photo{position:absolute;display:block}
.btn-olive{position:absolute;background:var(--olive);color:#fff;font:700 15px "Lato",sans-serif;display:flex;align-items:center;justify-content:center;text-transform:uppercase;letter-spacing:.2px}
.btn-outline{position:absolute;border:2px solid var(--ink);font:700 16px "Lato",sans-serif;display:flex;align-items:center;justify-content:center}
.dot{display:inline-block;width:14px;height:14px;border-radius:50%;background:#fff}

/* top bar */
.topbar{position:absolute;top:0;left:0;width:1200px;height:37px;background:var(--ink);color:#fff;font-size:14px}
.topbar .social{position:absolute;left:146px;top:11px;display:flex;gap:16px}
.topbar .msg{position:absolute;left:0;width:1200px;top:10px;text-align:center}

/* header */
.header{position:absolute;top:37px;left:0;width:1200px;height:123px;background:var(--olive)}
.brand{position:absolute;left:138px;top:30px;width:160px;text-align:center;color:#f1ecd9}
.brand .mark{width:36px;height:36px;border:2px solid #f1ecd9;border-radius:50%;margin:0 auto 8px}
.brand .name{font:400 22px "Mulish",sans-serif;letter-spacing:3px;text-transform:uppercase}
.search{position:absolute;left:378px;top:44px;width:344px;height:34px;border:1px solid #e9e9e9;color:#fff;font-size:13px;padding:9px 14px}
.search svg{position:absolute;right:10px;top:9px}
.account{position:absolute;left:788px;top:38px;color:#fff;font-size:13px;display:flex;gap:10px;align-items:center}
.account .ico{width:38px;height:38px;border-radius:50%;background:#fff}
.cart{position:absolute;left:938px;top:38px;color:#fff;font-size:13px;display:flex;gap:10px;align-items:center}
.cart .badge{position:absolute;left:26px;top:-6px;width:16px;height:16px;border-radius:50%;background:var(--ink);font-size:10px;text-align:center;line-height:16px}

/* nav */
.nav{position:absolute;top:160px;left:0;width:1200px;height:40px;background:var(--band);font-size:15px;color:var(--ink)}
.nav .left{position:absolute;left:156px;top:11px;display:flex;gap:28px}
.nav .right{position:absolute;left:865px;top:11px;display:flex;gap:30px}

/* hero */
.hero{position:absolute;top:200px;left:0;width:1200px;height:494px;background:linear-gradient(100deg,#6e7b58 0%,#8b9774 45%,#a39c86 70%,#7b8463 100%)}
.hero-title{position:absolute;left:198px;top:96px;color:#fff;font:300 42px/50px "Mulish",sans-serif}
.hero-arrows{position:absolute;left:200px;top:220px;display:flex;gap:10px}
.hero-arrows span{width:38px;height:38px;background:#fff;display:flex;align-items:center;justify-content:center}
.strip{position:absolute;top:694px;left:0;width:1200px;height:68px;background:var(--ink);color:#fff;font-size:18px}
.strip .item{position:absolute;top:18px;display:flex;align-items:center;gap:16px}
.strip .item b{font-weight:400;border:2px solid #fff;padding:5px 14px}

/* something new */
.new-title{position:absolute;left:137px;top:826px;font:800 40px/46px "Mulish",sans-serif;color:var(--ink)}
.new-copy{position:absolute;left:138px;top:926px;width:290px;font-size:13px;line-height:17px}
.cat{position:absolute;top:828px;width:298px}
.cat .img{height:196px;position:relative}
.cat .tag{position:absolute;left:20px;bottom:14px;background:rgba(255,255,255,.85);color:#555;font-size:15px;padding:5px 14px}
.cat.dark .tag{background:rgba(60,60,60,.55);color:#fff}
.cat h4{font:900 18px "Lato",sans-serif;margin-top:12px;color:var(--ink)}
.cat p{font-size:14px;margin-top:8px;white-space:nowrap}
.rule{position:absolute;left:137px;width:924px;height:1px;background:var(--line)}

/* featured */
.sec-title{position:absolute;left:0;width:1200px;text-align:center;font:800 38px "Mulish",sans-serif;color:var(--ink)}
.card{position:absolute;top:1275px;width:221px}
.card .img{height:337px;position:relative}
.card .eye{position:absolute;left:4px;bottom:0;width:36px;height:34px;background:var(--ink);display:flex;align-items:center;justify-content:center}
.card.olive-eye .eye{background:var(--olive)}
.card h5{font:400 19px/23px "Lato",sans-serif;margin-top:22px;color:var(--ink)}
.card .price{font-size:16px;margin-top:16px}
.swatches{display:flex;gap:6px;margin-top:22px}
.swatches i{width:26px;height:24px;display:block}
.sizes{display:flex;gap:4px;margin-top:14px}
.sizes span{width:24px;height:24px;border:1px solid #ddd;font-size:14px;display:flex;align-items:center;justify-content:center}
.sizes span.on{background:var(--ink);color:#fff;border-color:var(--ink)}
.slide-arrow{position:absolute;width:36px;height:36px;background:#fff;display:flex;align-items:center;justify-content:center}

/* big sale */
.sale-box{position:absolute;left:605px;top:1952px;width:458px;height:306px;background:#fff;border:1px solid var(--line);text-align:center}
.sale-box h3{font:700 38px "Barlow Semi Condensed",sans-serif;margin-top:22px;color:var(--ink)}
.sale-box p{font-size:18px;margin-top:4px;color:#333}
.timer{display:flex;gap:14px;justify-content:center;margin-top:22px}
.timer div{width:68px;height:72px;border:1.5px solid #888;padding-top:12px}
.timer b{display:block;font:800 24px "Mulish",sans-serif}
.timer small{font-size:11px;color:#555}
.block-title{position:absolute;font:700 40px "Barlow Semi Condensed",sans-serif;color:var(--ink);text-transform:uppercase;text-align:center}
.block-copy{position:absolute;font-size:14px;line-height:18px;text-align:center;color:#333}

/* features */
.feature{position:absolute;top:3876px;display:flex;gap:14px;align-items:center}
.feature h6{font:700 19px "Barlow Semi Condensed",sans-serif;color:var(--ink);text-transform:uppercase}
.feature p{font-size:11px;margin-top:4px;color:#444}

/* testimonials */
.reviews{position:absolute;top:4009px;left:0;width:1200px;height:479px;background:var(--olive)}
.review{position:absolute;top:96px;width:292px;text-align:center;color:#fff}
.review h6{font:600 22px "Barlow Semi Condensed",sans-serif;text-transform:uppercase}
.review p{font-size:13px;line-height:17px;margin-top:14px}
.review .avatar{width:84px;height:84px;border-radius:50%;margin:26px auto 0;background:radial-gradient(circle,#c9894e,#6e4428)}
.review .who{font:700 14px "Lato",sans-serif;margin-top:22px}
.review .stars{margin-top:10px;letter-spacing:8px;font-size:18px}

/* brands */
.brands{position:absolute;top:4632px;left:160px;width:880px;display:flex;justify-content:space-between;align-items:center}
.brands span{font:900 34px "Lato",sans-serif;color:var(--ink)}
.brands span.sm{font-size:20px}

/* newsletter */
.newsletter{position:absolute;top:4743px;left:0;width:1200px;height:153px;background:var(--ink);color:#fff}
.newsletter h3{position:absolute;left:137px;top:42px;font:600 38px "Barlow Semi Condensed",sans-serif}
.newsletter p{position:absolute;left:139px;top:96px;font:700 13px "Lato",sans-serif}
.nl-input{position:absolute;left:608px;top:48px;width:290px;height:48px;border:1px solid #aaa;font-size:14px;padding:16px 18px;color:#ccc}
.nl-btn{position:absolute;left:898px;top:48px;width:164px;height:48px;background:#fff;color:var(--olive-dark);font:800 21px "Mulish",sans-serif;display:flex;align-items:center;justify-content:center}

/* footer */
.footer{position:absolute;top:4896px;left:0;width:1200px;height:363px;background:var(--footer)}
.fcol{position:absolute;top:66px}
.fcol h6{font:700 29px "Barlow Semi Condensed",sans-serif;color:var(--ink);text-transform:uppercase}
.fcol p,.fcol li{font-size:13px;line-height:17px;color:#333}
.fcol ul{list-style:none;margin-top:16px}
.fcol li{margin-bottom:12px}
.fcol .row{display:flex;gap:12px;align-items:center;margin-top:13px;font-size:13px}
.copy{position:absolute;left:142px;top:332px;font-size:13px}
.pay{position:absolute;left:842px;top:312px;display:flex;gap:6px}
.pay i{width:30px;height:18px;border:1px solid #ccc;background:#fff;display:block;border-radius:2px}
</style>
</head>
<body>

<!-- top bar -->
<div class="topbar">
  <div class="social"><span class="dot"></span><span class="dot"></span><span class="dot"></span><span class="dot"></span></div>
  <div class="msg">Sale is on 40% off on all products</div>
</div>

<!-- header -->
<header class="header">
  <div class="brand"><div class="mark"></div><div class="name">Copper Dunes</div></div>
  <div class="search">Search
    <svg width="14" height="14" viewBox="0 0 14 14"><circle cx="6" cy="6" r="4.5" fill="none" stroke="#fff" stroke-width="1.5"/><path d="M9.5 9.5 13 13" stroke="#fff" stroke-width="1.5"/></svg>
  </div>
  <div class="account"><div class="ico"></div><div>My Account<br>Log in</div></div>
  <div class="cart" style="position:absolute">
    <svg width="38" height="38" viewBox="0 0 38 38"><circle cx="19" cy="19" r="19" fill="#fff"/><path d="M10 12h3l3 11h10l2-8H15" fill="none" stroke="#6f7b5c" stroke-width="2"/><circle cx="17" cy="27" r="1.6" fill="#6f7b5c"/><circle cx="25" cy="27" r="1.6" fill="#6f7b5c"/></svg>
    <span class="badge">0</span>
    <div>Cart<br>€0,00 EUR</div>
  </div>
</header>

<nav class="nav">
  <div class="left"><span>New arrivals</span><span>Shop</span><span>Collections</span><span>Testimonials</span><span>FAQ</span></div>
  <div class="right"><span>Special offers</span><span>Contact us</span></div>
</nav>

<!-- hero -->
<section class="hero" role="img" aria-label="Woman in a white suit with sunglasses seated in a brown leather armchair">
  <h1 class="hero-title">The Signature<br>Collections</h1>
  <div class="hero-arrows">
    <span><svg width="12" height="12" viewBox="0 0 12 12"><path d="M8 1 3 6l5 5" fill="none" stroke="#222" stroke-width="1.6"/></svg></span>
    <span><svg width="12" height="12" viewBox="0 0 12 12"><path d="M4 1l5 5-5 5" fill="none" stroke="#222" stroke-width="1.6"/></svg></span>
  </div>
</section>
<div class="strip">
  <div class="item" style="left:110px">Grand opening offers: Sale is now on up to 40% off <b>See All</b></div>
  <div class="item" style="left:680px">Grand opening offers: Sale is now on up to 40% off <b>See All</b></div>
</div>

<!-- something new -->
<h2 class="new-title">Something New<br>From Fashion</h2>
<p class="new-copy">Lorem ipsum dolor sit amet, consectetur adipiscing elit, sed do eiusmod tempor incididunt ut labore et dolore magna aliqua.</p>
<div class="btn-outline" style="left:138px;top:1011px;width:92px;height:40px">See All</div>

<div class="cat" style="left:448px">
  <div class="img" role="img" aria-label="Woman in white outfit seated on a stool" style="background:linear-gradient(180deg,#e6e4e0,#c9c6c0)"><span class="tag">Discover</span></div>
  <h4>Women</h4><p>Discover women's fashion and style.</p>
</div>
<div class="cat dark" style="left:763px">
  <div class="img" role="img" aria-label="Man in red swim shorts on a pool float" style="background:linear-gradient(135deg,#1f7fa8,#3aa6c9 60%,#d44a3a)"><span class="tag">Discover</span></div>
  <h4>Men</h4><p>Discover men's swimwear</p>
</div>
<div class="cat dark" style="left:1078px;width:122px;overflow:hidden">
  <div class="img" role="img" aria-label="Girl with colourful beach toys" style="background:linear-gradient(135deg,#f2a33a,#e07a2c)"><span class="tag">Discover</span></div>
  <h4>Children</h4><p>Discover women's</p>
</div>

<div class="rule" style="top:1128px"></div>

<!-- featured -->
<h2 class="sec-title" style="top:1180px">Featured Collection</h2>

<div class="card" style="left:141px">
  <div class="img" role="img" aria-label="Woman in a pink blazer and shorts" style="background:linear-gradient(180deg,#efeeec,#dcd8d4)"><span class="eye"><span class="dot" style="width:10px;height:10px"></span></span></div>
  <h5>Organic Cotton Tailored Shorts Pair for Women</h5>
  <div class="price">€217,95 EUR</div>
  <div class="swatches"><i style="background:#d9aab8"></i><i style="background:#e0e0e0"></i><i style="background:#8b5e3c"></i></div>
  <div class="sizes"><span class="on">S</span><span>M</span></div>
</div>
<div class="card olive-eye" style="left:374px">
  <div class="img" role="img" aria-label="Woman in a long white dress" style="background:linear-gradient(180deg,#eeeeee,#dadada)"><span class="eye"><span class="dot" style="width:10px;height:10px"></span></span></div>
  <h5>Double the Warmth Girl's Fashion</h5>
  <div class="price">€217,95 EUR</div>
  <div class="swatches"><i style="background:#bcd0f0"></i><i style="background:#e8ecef"></i><i style="background:#5f7052"></i></div>
  <div class="sizes"><span class="on">S</span><span>M</span></div>
</div>
<div class="card olive-eye" style="left:607px">
  <div class="img" role="img" aria-label="Woman in a floral mini dress" style="background:linear-gradient(180deg,#f1f0ee,#dedbd7)"><span class="eye"><span class="dot" style="width:10px;height:10px"></span></span></div>
  <h5>Double the Warmth Girl's Fashion</h5>
  <div class="price">€217,95 EUR</div>
  <div class="swatches"><i style="background:#7d4d63"></i><i style="background:#f08a98"></i><i style="background:#8b5e3c"></i></div>
  <div class="sizes"><span class="on">S</span><span>M</span><span>L</span></div>
</div>
<div class="card olive-eye" style="left:840px">
  <div class="img" role="img" aria-label="Woman in a black coat and trousers" style="background:linear-gradient(180deg,#f1f1f1,#dcdcdc)"><span class="eye"><span class="dot" style="width:10px;height:10px"></span></span></div>
  <h5>Organic Cotton Tailored Shorts Pair for Women</h5>
  <div class="price">€217,95 EUR</div>
  <div class="swatches"><i style="background:#d9aab8"></i><i style="background:#e0e0e0"></i><i style="background:#8b5e3c"></i></div>
  <div class="sizes"><span class="on">S</span><span>M</span></div>
</div>
<span class="slide-arrow" style="left:142px;top:1486px"><svg width="12" height="12" viewBox="0 0 12 12"><path d="M8 1 3 6l5 5" fill="none" stroke="#222" stroke-width="1.6"/></svg></span>
<span class="slide-arrow" style="left:1022px;top:1484px;background:var(--olive-dark)"><svg width="12" height="12" viewBox="0 0 12 12"><path d="M4 1l5 5-5 5" fill="none" stroke="#fff" stroke-width="1.6"/></svg></span>

<div class="rule" style="top:1860px"></div>

<!-- big sale -->
<div class="photo" role="img" aria-label="Two women in utility jumpsuits against a beige wall" style="left:137px;top:1913px;width:541px;height:384px;background:linear-gradient(90deg,#c9b9a4,#ddd0bf 60%,#6f7b5c)"></div>
<div class="sale-box">
  <h3>BIG SALE</h3>
  <p>The best collection of the week</p>
  <div class="timer">
    <div><b>45</b><small>Days</small></div>
    <div><b>6</b><small>Hours</small></div>
    <div><b>3</b><small>Mins</small></div>
    <div><b>8</b><small>Sec</small></div>
  </div>
  <div class="btn-olive" style="left:113px;top:218px;width:230px;height:46px;position:absolute">Shop the collection</div>
</div>

<!-- exclusive -->
<h2 class="block-title" style="left:150px;top:2458px;width:440px">Exclusive Collection</h2>
<p class="block-copy" style="left:140px;top:2514px;width:460px">All the online shopping services available during the holiday season</p>
<div class="btn-olive" style="left:262px;top:2560px;width:230px;height:46px">Shop the collection</div>
<div class="photo" role="img" aria-label="Two girls in swimsuits splashing by a pool" style="left:600px;top:2346px;width:600px;height:380px;background:linear-gradient(120deg,#9bc7d6,#5aa9c7 50%,#d9b79a)"></div>

<!-- men's -->
<div class="photo" role="img" aria-label="Man in sunglasses and orange swim shorts by a pool" style="left:137px;top:2770px;width:564px;height:437px;background:linear-gradient(135deg,#2cb3d6,#7fd3e6 55%,#e86a33)"></div>
<h2 class="block-title" style="left:720px;top:2860px;width:360px">Men's Swimwear</h2>
<p class="block-copy" style="left:726px;top:2928px;width:340px">Lorem ipsum dolor sit amet, consectetur adipiscing elit, sed do eiusmod tempor incididunt ut labore et dolore magna aliqua.</p>
<div class="btn-olive" style="left:780px;top:3010px;width:230px;height:46px">Shop the collection</div>

<!-- children -->
<h2 class="block-title" style="left:170px;top:3376px;width:290px;line-height:44px">Children<br>Swimwear</h2>
<p class="block-copy" style="left:192px;top:3482px;width:250px">Lorem ipsum dolor sit amet, consectetur adipiscing elit, sed do eiusmod tempor incididunt ut labore et dolore magna aliqua.</p>
<span class="slide-arrow" style="left:140px;top:3486px;border:1px solid #444"><svg width="12" height="12" viewBox="0 0 12 12"><path d="M8 1 3 6l5 5" fill="none" stroke="#222" stroke-width="1.6"/></svg></span>
<div class="photo" role="img" aria-label="Girl in a pastel floral swimsuit" style="left:458px;top:3257px;width:328px;height:534px;background:linear-gradient(180deg,#f1efed,#e3dfdc)"></div>
<div class="photo" role="img" aria-label="Boy with swim goggles on a blue background" style="left:800px;top:3257px;width:262px;height:370px;background:linear-gradient(180deg,#5ab0ea,#4aa4e2)"><span style="position:absolute;left:4px;bottom:0;width:36px;height:34px;background:var(--ink);display:flex;align-items:center;justify-content:center"><span class="dot" style="width:10px;height:10px"></span></span></div>
<div class="abs" style="left:802px;top:3640px;font-size:18px">Swimwear</div>
<div class="abs" style="left:802px;top:3668px;font-size:15px">€109,95 EUR</div>
<div class="abs sizes" style="left:802px;top:3690px"><span class="on">S</span><span>M</span></div>
<div class="abs" style="left:802px;top:3740px;width:136px;height:38px;background:var(--ink);color:#fff;font:700 12px 'Lato',sans-serif;display:flex;align-items:center;justify-content:center">ADD TO CART</div>

<!-- features -->
<div class="feature" style="left:136px">
  <svg width="80" height="56" viewBox="0 0 80 56"><path d="M4 10h44v30H4zM48 20h16l10 12v8H48z" fill="none" stroke="#555" stroke-width="2"/><circle cx="18" cy="44" r="6" fill="#fff" stroke="#555" stroke-width="2"/><circle cx="60" cy="44" r="6" fill="#fff" stroke="#555" stroke-width="2"/></svg>
  <div><h6>Free shipping</h6><p>Picking lists and shipping with Rivo Mail</p></div>
</div>
<div class="feature" style="left:484px">
  <svg width="50" height="50" viewBox="0 0 50 50"><rect x="6" y="18" width="38" height="18" fill="none" stroke="#555" stroke-width="2"/><rect x="14" y="8" width="22" height="10" fill="none" stroke="#555" stroke-width="2"/><rect x="14" y="30" width="22" height="14" fill="#fff" stroke="#555" stroke-width="2"/></svg>
  <div><h6>Label printing</h6><p>New online special festival offer</p></div>
</div>
<div class="feature" style="left:780px">
  <svg width="50" height="50" viewBox="0 0 50 50"><path d="M40 25a15 15 0 1 1-6-12" fill="none" stroke="#555" stroke-width="2"/><path d="M18 25l5 5 10-10" fill="none" stroke="#555" stroke-width="2"/><text x="26" y="47" font-family="Lato" font-size="14" fill="#555">24</text></svg>
  <div><h6>24x7 service</h6><p>Online service for new customer</p></div>
</div>

<!-- testimonials -->
<section class="reviews">
  <div class="review" style="left:140px">
    <h6>Stunning design</h6>
    <p>Lorem ipsum dolor sit amet, consectetur adipiscing elit, sed do eiusmod tempor incididunt ut labore et dolore magna aliqua. Quis ipsum suspendisse ultrices gravida. Risus commodo viverra maecenas accumsan lacus vel facilisis.</p>
    <div class="avatar" role="img" aria-label="Customer portrait"></div>
    <div class="who">Mira Solen</div><div class="stars">★★★★★</div>
  </div>
  <div class="review" style="left:454px">
    <h6>Comfortable to wear</h6>
    <p>Lorem ipsum dolor sit amet, consectetur adipiscing elit, sed do eiusmod tempor incididunt ut labore et dolore magna aliqua. Quis ipsum suspendisse ultrices gravida. Risus commodo viverra maecenas accumsan lacus vel facilisis.</p>
    <div class="avatar" role="img" aria-label="Customer portrait" style="background:radial-gradient(circle,#7fb9c9,#3f6f7f)"></div>
    <div class="who">Mira Solen</div><div class="stars">★★★★★</div>
  </div>
  <div class="review" style="left:764px">
    <h6>Good for winter wear</h6>
    <p>Lorem ipsum dolor sit amet, consectetur adipiscing elit, sed do eiusmod tempor incididunt ut labore et dolore magna aliqua. Quis ipsum suspendisse ultrices gravida. Risus commodo viverra maecenas accumsan lacus vel facilisis.</p>
    <div class="avatar" role="img" aria-label="Customer portrait" style="background:radial-gradient(circle,#f0a35a,#c2542a)"></div>
    <div class="who">Mira Solen</div><div class="stars">★★★★★</div>
  </div>
</section>

<!-- brands -->
<h2 class="sec-title" style="top:4548px;font:700 38px 'Barlow Semi Condensed',sans-serif">BRANDS</h2>
<div class="brands">
  <span>Strido</span><span>Kelvo</span><span class="sm">Marlow</span><span>Vexa</span><span class="sm">Northline</span><span class="sm">Tremont</span>
</div>

<!-- newsletter -->
<section class="newsletter">
  <h3>NEWSLETTER</h3>
  <p>Use this text to share information about brand with customers.</p>
  <div class="nl-input">Email</div>
  <div class="nl-btn">Subscribe</div>
</section>

<!-- footer -->
<footer class="footer">
  <div class="fcol" style="left:142px;width:280px">
    <h6>About us</h6>
    <p style="margin-top:16px">Lorem ipsum dolor sit amet, consectetur adipiscing elit, sed do eiusmod tempor incididunt ut labore et dolore magna aliqua. Quis ipsum suspendisse ultrices gravida. Risus commodo viverra maecenas accumsan lacus vel facilisis.</p>
    <div style="display:flex;gap:12px;margin-top:26px"><span class="dot" style="background:#333;width:12px;height:12px"></span><span class="dot" style="background:#333;width:12px;height:12px"></span><span class="dot" style="background:#333;width:12px;height:12px"></span><span class="dot" style="background:#333;width:12px;height:12px"></span></div>
  </div>
  <div class="fcol" style="left:448px">
    <h6>Products</h6>
    <ul><li>Featured products</li><li>Bestseller</li><li>Latest product</li><li>All collections</li><li>All products</li></ul>
  </div>
  <div class="fcol" style="left:656px">
    <h6>Menu</h6>
    <ul><li>Search</li><li>About us</li><li>Contact us</li><li>Blogs</li><li>FAQ</li></ul>
  </div>
  <div class="fcol" style="left:828px">
    <h6>Contact us</h6>
    <p style="margin-top:16px">Available between 8AM to 8PM.<br>Ready to answer your questions.</p>
    <div class="row"><svg width="12" height="14" viewBox="0 0 12 14"><path d="M6 13S1 8 1 5a5 5 0 0 1 10 0c0 3-5 8-5 8z" fill="#6f7b5c"/></svg>27 Harbour View Rd</div>
    <div class="row"><svg width="12" height="12" viewBox="0 0 12 12"><path d="M2 1h3l1 3-2 1a7 7 0 0 0 3 3l1-2 3 1v3c-6 0-9-3-9-9z" fill="#6f7b5c"/></svg>(555) 014-2290</div>
    <div class="row"><svg width="13" height="10" viewBox="0 0 13 10"><rect x=".5" y=".5" width="12" height="9" fill="#6f7b5c"/><path d="M1 1l5.5 4L12 1" fill="none" stroke="#fff"/></svg>hello@copperdunes.com</div>
  </div>
  <div class="copy">© 2025, &nbsp;| &nbsp;www.copperdunes.com</div>
  <div class="pay"><i></i><i></i><i></i><i></i><i></i><i></i></div>
  <div class="abs" style="left:1096px;top:330px;font-size:11px">M1</div>
</footer>

</body>
</html>
```